Wordpress Lifestyle Blog

Just to be clear - I have the domain and the wordpress site (which is messy). I need someone to help me complete a Plainleaf blog design and then go into the existing wordpress site, and get rid of all the existing rubbish and set up the templates please. If we progress with design can we please be clear about additional costs upfront which, of course, I appreciate is the case.

Need a lifestyle blog. It is called brightyearsahead.com. Aimed at the older woman but needs to look fresh and young, not old fashioned. Navigation will be Home, Fashion, Feelings, Fitness, Contact. I have a logo but not sure it will work at the moment so happy with stylised words.Will have social media links.

Need homepage (not overly long) to have a main slider for pics/videos. Then the three category boxes underneath linking through to 2nd level pages containing blogs for that category and then the actual blog page. Happy to be led by expertise if this is not gonna work.

Am really looking for something clean and fresh like a Marwyn type approach to be honest.

If you need any further direction please just ask - once design chosen I am looking to move quickly.

Thank you so much for looking at this brief

Target Market(s)

Women, 40 - 60 age group but with a younger outlook

Number of Pages Required

3 page

Colors

Designer to choose colors to be used in the design.

Requirements
Must have
• Reflect youth, fun, bright
• Lift easily into a wordpress format
Should not have
• Old, staid, frumpy,dark

```html
<!DOCTYPE html>
<html lang="en">
<head>
<meta charset="utf-8">
<title>brightyearsahead.com</title>
<link href="https://fonts.googleapis.com/css2?family=Play:wght@400;700&family=Arimo:wght@400;700&family=Raleway:wght@300;400;500&family=Playball&display=swap" rel="stylesheet">
<style>
:root{
  --blue:#3a9fd1;
  --green:#2ea14a;
  --ink:#1f1f1f;
  --text:#333;
  --muted:#666;
  --panel:#e3e3e3;
  --line:#d6d6d6;
  --white:#fff;
  --pink:#d6337a;
}
*{box-sizing:border-box;margin:0;padding:0}
html,body{width:1200px;height:2736px;overflow:hidden;background:var(--white)}
body{font-family:"Arimo",Arial,sans-serif;color:var(--text);position:relative}
.abs{position:absolute}

/* header */
.follow{left:173px;top:14px;display:flex;align-items:center;gap:7px;font:700 14px "Arimo",sans-serif;color:var(--ink)}
.follow .dot{width:30px;height:30px;border-radius:50%;background:var(--blue)}
.follow .dot.alt{background:#56a9d6}
.follow .dot.grey{background:#8a8a8a}
.search{left:812px;top:9px;width:212px;height:32px;border:1px solid #cfcfcf;display:flex}
.search span{flex:1;font:13px "Arimo",sans-serif;color:#888;padding:7px 8px}
.search .btn{width:30px;background:var(--green);display:flex;align-items:center;justify-content:center}
.brand{left:173px;top:64px;font:700 27px "Play",sans-serif;color:var(--blue);white-space:nowrap}
.nav{left:529px;top:74px;font:700 16px "Play",sans-serif;color:var(--ink)}
.nav a{position:absolute;white-space:nowrap;text-decoration:none;color:var(--ink)}
.nav a.active{color:var(--green)}

/* hero */
.hero{left:0;top:119px;width:1200px;height:474px;background:linear-gradient(180deg,#8fb8df 0%,#cfe0ee 30%,#7fcad0 42%,#3fb1bd 52%,#e8e2d6 66%,#d9cfbf 100%)}
.hero .arrow{position:absolute;top:201px;width:30px;height:30px;background:#222;display:flex;align-items:center;justify-content:center}
.hero .caption{position:absolute;left:0;bottom:0;width:100%;height:50px;background:rgba(0,0,0,.55);color:var(--white);font:700 23.5px "Play",sans-serif;padding:10px 0 0 173px;white-space:nowrap}

/* categories */
.cat{top:616px;width:278px;height:165px;border-radius:6px;overflow:hidden;color:var(--white);font:700 23px "Play",sans-serif;text-align:center}
.cat .bg{position:absolute;inset:0}
.cat .shade{position:absolute;inset:0;background:rgba(0,0,0,.35)}
.cat .label{position:absolute;left:0;right:0;top:50px}
.cat svg{display:block;margin:0 auto 8px}

/* posts */
.post{left:173px;width:589px;height:430px}
.date{left:0;top:0;width:64px;height:67px;background:#ececec;text-align:center;font:15px "Arimo",sans-serif;color:var(--ink);padding-top:12px;line-height:21px}
.post-title{left:84px;top:1px;font:700 23px "Play",sans-serif;color:var(--blue);white-space:nowrap}
.post-sub{left:84px;top:36px;font:11.5px "Arimo",sans-serif;color:var(--text)}
.post-img{left:0;top:68px;width:589px;height:186px}
.post-body{left:0;top:268px;width:589px;font:12.2px/19.5px "Arimo",sans-serif;color:var(--text)}
.meta{left:0;top:379px;width:589px;height:30px;border-bottom:1px solid var(--line);font:11px "Raleway",sans-serif;color:var(--muted)}
.meta .item{position:absolute;top:6px;display:flex;align-items:center;gap:7px}
.meta .read{position:absolute;right:0;top:2px;width:87px;height:26px;background:var(--blue);color:var(--white);font:500 11px "Raleway",sans-serif;text-align:center;line-height:26px}
.load{left:173px;top:2636px;width:589px;height:38px;border:1px solid #bbb;border-radius:4px;font:12px "Raleway",sans-serif;color:var(--text);display:flex;align-items:center;justify-content:center;gap:8px}
.footer{left:0;top:2694px;width:1200px;height:42px;background:var(--blue);color:var(--white);font:11.5px "Raleway",sans-serif;text-align:center;line-height:42px}

/* sidebar */
.side{left:788px;width:241px}
.signup{top:824px;height:157px;background:var(--panel);padding:16px 18px}
.signup p{font:700 13px/21px "Arimo",sans-serif;color:var(--ink)}
.field{background:var(--white);border:1px solid #bcbcbc;height:33px;font:italic 11.5px "Arimo",sans-serif;color:#999;padding:9px 10px}
.signup .field{margin-top:12px;width:205px}
.btn-blue{display:inline-block;margin-top:12px;background:var(--blue);color:var(--white);font:500 11px "Raleway",sans-serif;padding:9px 12px}
.side-head{font:700 25px "Play",sans-serif;color:var(--ink)}
.recent{top:1076px;height:188px;background:var(--panel);padding:8px 10px 0 10px}
.recent li{list-style:none;display:flex;gap:8px;font:11px/19px "Arimo",sans-serif;color:var(--text);margin-bottom:5px}
.recent li b{color:var(--green);font-size:14px}
.recent .all{position:absolute;right:0;bottom:-12px;background:var(--blue);color:var(--white);font:500 11px "Raleway",sans-serif;padding:8px 12px}
.social{top:1306px;height:336px;border:1px solid var(--line)}
.tabs{display:flex;height:30px;border-bottom:1px solid var(--line);font:11.5px "Arimo",sans-serif;color:var(--ink)}
.tabs span{display:flex;align-items:center;gap:5px;padding:0 6px}
.tabs span.on{background:var(--white)}
.tabs span.off{background:#efefef}
.tabs i{width:14px;height:14px;border-radius:50%;border:1px solid #777;display:inline-block}
.feed{padding:0 10px}
.feed .row{display:flex;gap:10px;margin-top:16px;height:52px}
.feed .avatar{width:51px;height:51px;flex:none}
.feed p{font:10px/15px "Arimo",sans-serif;color:var(--text)}
.feed .like{display:inline-block;margin-top:4px;border:1px solid #b9c4d8;background:#f2f4f8;font:9px "Arimo",sans-serif;color:#3b5a94;padding:1px 5px}
.query{top:1674px;height:256px;background:var(--panel);padding:14px 20px}
.query h4{font:700 19px "Play",sans-serif;color:var(--ink)}
.query .field{margin-top:10px;width:205px}
.query .area{height:76px}
.btn-green{display:inline-block;margin-top:14px;background:var(--green);color:var(--white);font:700 16px "Play",sans-serif;padding:6px 14px}
.tags{top:2003px;height:171px;background:var(--panel);padding:12px 10px;font-family:"Raleway",sans-serif;color:#333;line-height:28px}
.tags span{margin-right:3px}
.ad{top:2207px;height:296px;border:1px solid #bdbdbd;border-radius:8px;overflow:hidden;text-align:center}
.ad .maker{position:absolute;left:6px;top:6px;font:700 15px "Play",sans-serif;color:var(--green)}
.ad .photo{position:absolute;left:20px;top:32px;width:200px;height:188px;background:linear-gradient(160deg,#e9f0d8,#a8c85a 45%,#4f7f24)}
.ad .tag1{position:absolute;left:0;right:0;top:226px;font:30px "Playball",cursive;color:var(--pink)}
.ad .tag2{position:absolute;left:0;right:0;top:264px;font:700 19px "Arimo",sans-serif;color:var(--green)}
</style>
</head>
<body>

<header>
  <div class="abs follow">Follow Us On
    <span class="dot" aria-label="Friends"></span>
    <span class="dot alt" aria-label="Chirps"></span>
    <span class="dot grey" aria-label="Snaps"></span>
  </div>
  <div class="abs search"><span>Search here</span>
    <div class="btn"><svg width="16" height="16" viewBox="0 0 16 16"><circle cx="6.5" cy="6.5" r="4.5" fill="none" stroke="#fff" stroke-width="2"/><line x1="10" y1="10" x2="14" y2="14" stroke="#fff" stroke-width="2"/></svg></div>
  </div>
  <div class="abs brand">brightyearsahead.com</div>
  <nav class="abs nav">
    <a class="active" style="left:0">Home</a>
    <a style="left:82px">Fashion</a>
    <a style="left:179px">Feeling</a>
    <a style="left:268px">Fitness</a>
    <a style="left:361px">About</a>
    <a style="left:447px">Contact</a>
  </nav>
</header>

<section class="abs hero" role="img" aria-label="Couple relaxing in deck chairs on a tropical beach">
  <div class="arrow" style="left:8px"><svg width="12" height="14"><path d="M9 1 3 7l6 6" fill="none" stroke="#fff" stroke-width="2.5"/></svg></div>
  <div class="arrow" style="right:8px"><svg width="12" height="14"><path d="M3 1l6 6-6 6" fill="none" stroke="#fff" stroke-width="2.5"/></svg></div>
  <div class="caption">Lorem Ipsum Dolor Sit Ametem Ipsum Dolor Sit Ame Ecit Adipi&nbsp; Consecit Adipi</div>
</section>

<section>
  <a class="abs cat" style="left:173px">
    <div class="bg" role="img" aria-label="Woman with a colourful umbrella by the sea" style="background:linear-gradient(160deg,#6f8a9e,#44525a 60%,#5c4a3c)"></div>
    <div class="shade"></div>
    <div class="label"><svg width="44" height="44" viewBox="0 0 44 44"><circle cx="22" cy="22" r="19" fill="none" stroke="#fff" stroke-width="3"/><circle cx="15" cy="17" r="2.5" fill="#fff"/><circle cx="29" cy="17" r="2.5" fill="#fff"/><path d="M12 25q10 10 20 0" fill="none" stroke="#fff" stroke-width="3"/></svg>FEELING</div>
  </a>
  <a class="abs cat" style="left:461px">
    <div class="bg" role="img" aria-label="Family walking on a beach" style="background:linear-gradient(160deg,#8c9ba3,#5a656a 60%,#6d6254)"></div>
    <div class="shade"></div>
    <div class="label"><svg width="44" height="44" viewBox="0 0 44 44"><circle cx="22" cy="12" r="8" fill="#fff"/><line x1="22" y1="20" x2="22" y2="42" stroke="#fff" stroke-width="3"/><path d="M22 28 12 20M22 28l10-8M22 34 14 30M22 34l8-4" stroke="#fff" stroke-width="2.5" fill="none"/></svg>FASHION</div>
  </a>
  <a class="abs cat" style="left:751px">
    <div class="bg" role="img" aria-label="Woman doing a yoga pose at sunset" style="background:linear-gradient(160deg,#a9b1ad,#616b68 60%,#403d36)"></div>
    <div class="shade"></div>
    <div class="label"><svg width="44" height="44" viewBox="0 0 44 44"><circle cx="22" cy="9" r="6" fill="#fff"/><path d="M14 18h16l-3 12h-10z" fill="#fff"/><rect x="6" y="34" width="32" height="6" rx="3" fill="#fff"/></svg>FITNESS</div>
  </a>
</section>

<main>
  <article class="abs post" style="top:824px">
    <div class="abs date">02<br>JAN</div>
    <h2 class="abs post-title">Lorem ipsum dolor sit amet, consecit adipi</h2>
    <p class="abs post-sub">Duis aute irure dolor in reprehenderit</p>
    <div class="abs post-img" role="img" aria-label="Suspension bridge at sunset over a bay" style="background:linear-gradient(180deg,#9a6fa8,#e07c8a 45%,#d99a7a 62%,#5a6aa0 80%,#3d4c7c)"></div>
    <p class="abs post-body">Lorem ipsum dolor sit amet, consecit adipiscing elit, sed do eiusmod tempor incidimen labore n dolorme laboris ni ut aliquip ex ena lin consequat Duis aute irure dolor in reprehenderit magna aliqua. Ut enim ad qnexercitation ullamco Neque porro quisquam est, qui dolorem ipsum quia dolor sit amet, conadipi velit sed quia non numquam eius modi tempora incidunt. Quis autem vel eum iure repremInderit in voluptate velit esse quam nihil molestiae consequatur.</p>
    <div class="abs meta">
      <span class="item" style="left:0"><svg width="13" height="13"><rect x="1" y="2" width="10" height="10" fill="none" stroke="#2ea14a" stroke-width="1.6"/><path d="M4 7l2 2 6-7" fill="none" stroke="#2ea14a" stroke-width="1.6"/></svg>Admin</span>
      <span class="item" style="left:113px"><svg width="14" height="13"><ellipse cx="7" cy="6" rx="6.5" ry="5" fill="#2ea14a"/><path d="M3 10l-1 3 4-2z" fill="#2ea14a"/></svg>Leave A Comment</span>
      <span class="item" style="left:292px"><svg width="13" height="13"><rect x="1" y="6" width="3" height="7" fill="#2ea14a"/><path d="M5 6l3-5q2 0 1 4h4v4l-2 4H5z" fill="#2ea14a"/></svg>Like Us</span>
      <span class="item" style="left:411px"><svg width="12" height="13"><circle cx="9" cy="2.5" r="2" fill="#2ea14a"/><circle cx="2.5" cy="6.5" r="2" fill="#2ea14a"/><circle cx="9" cy="10.5" r="2" fill="#2ea14a"/><path d="M9 2.5 2.5 6.5 9 10.5" fill="none" stroke="#2ea14a"/></svg>Share</span>
      <span class="read">READ MORE</span>
    </div>
  </article>

  <article class="abs post" style="top:1278px">
    <div class="abs date">02<br>JAN</div>
    <h2 class="abs post-title">Lorem ipsum dolor sit amet</h2>
    <p class="abs post-sub">Duis aute irure dolor in reprehenderit</p>
    <div class="abs post-img" role="img" aria-label="Man with a laptop sitting on a mountain ledge above the clouds" style="background:linear-gradient(180deg,#cfe2ef,#9ac0d8 35%,#3f73a6 62%,#23456e 80%,#5a5048)"></div>
    <p class="abs post-body">Lorem ipsum dolor sit amet, consecit adipiscing elit, sed do eiusmod tempor incidimen labore n dolorme laboris ni ut aliquip ex ena lin consequat Duis aute irure dolor in reprehenderit magna aliqua. Ut enim ad qnexercitation ullamco Neque porro quisquam est, qui dolorem ipsum quia dolor sit amet, conadipi velit sed quia non numquam eius modi tempora incidunt. Quis autem vel eum iure repremInderit in voluptate velit esse quam nihil molestiae consequatur.</p>
    <div class="abs meta">
      <span class="item" style="left:0"><svg width="13" height="13"><rect x="1" y="2" width="10" height="10" fill="none" stroke="#2ea14a" stroke-width="1.6"/><path d="M4 7l2 2 6-7" fill="none" stroke="#2ea14a" stroke-width="1.6"/></svg>Admin</span>
      <span class="item" style="left:113px"><svg width="14" height="13"><ellipse cx="7" cy="6" rx="6.5" ry="5" fill="#2ea14a"/><path d="M3 10l-1 3 4-2z" fill="#2ea14a"/></svg>Leave A Comment</span>
      <span class="item" style="left:292px"><svg width="13" height="13"><rect x="1" y="6" width="3" height="7" fill="#2ea14a"/><path d="M5 6l3-5q2 0 1 4h4v4l-2 4H5z" fill="#2ea14a"/></svg>Like Us</span>
      <span class="item" style="left:411px"><svg width="12" height="13"><circle cx="9" cy="2.5" r="2" fill="#2ea14a"/><circle cx="2.5" cy="6.5" r="2" fill="#2ea14a"/><circle cx="9" cy="10.5" r="2" fill="#2ea14a"/><path d="M9 2.5 2.5 6.5 9 10.5" fill="none" stroke="#2ea14a"/></svg>Share</span>
      <span class="read">READ MORE</span>
    </div>
  </article>

  <article class="abs post" style="top:1732px">
    <div class="abs date">05<br>JAN</div>
    <h2 class="abs post-title">Lorem ipsum dolor sit amet, consecit adipi</h2>
    <p class="abs post-sub">Duis aute irure dolor in reprehenderit</p>
    <div class="abs post-img" role="img" aria-label="Fresh vegetables around a heart-shaped chalk board about mindful eating" style="background:linear-gradient(90deg,#3c5a2c,#6c8a3e 30%,#3a3532 50%,#b84a2e 75%,#8a2e22)"></div>
    <p class="abs post-body">Lorem ipsum dolor sit amet, consecit adipiscing elit, sed do eiusmod tempor incidimen labore n dolorme laboris ni ut aliquip ex ena lin consequat Duis aute irure dolor in reprehenderit magna aliqua. Ut enim ad qnexercitation ullamco Neque porro quisquam est, qui dolorem ipsum quia dolor sit amet, conadipi velit sed quia non numquam eius modi tempora incidunt. Quis autem vel eum iure repremInderit in voluptate velit esse quam nihil molestiae consequatur.</p>
    <div class="abs meta">
      <span class="item" style="left:0"><svg width="13" height="13"><rect x="1" y="2" width="10" height="10" fill="none" stroke="#2ea14a" stroke-width="1.6"/><path d="M4 7l2 2 6-7" fill="none" stroke="#2ea14a" stroke-width="1.6"/></svg>Admin</span>
      <span class="item" style="left:113px"><svg width="14" height="13"><ellipse cx="7" cy="6" rx="6.5" ry="5" fill="#2ea14a"/><path d="M3 10l-1 3 4-2z" fill="#2ea14a"/></svg>Leave A Comment</span>
      <span class="item" style="left:292px"><svg width="13" height="13"><rect x="1" y="6" width="3" height="7" fill="#2ea14a"/><path d="M5 6l3-5q2 0 1 4h4v4l-2 4H5z" fill="#2ea14a"/></svg>Like Us</span>
      <span class="item" style="left:411px"><svg width="12" height="13"><circle cx="9" cy="2.5" r="2" fill="#2ea14a"/><circle cx="2.5" cy="6.5" r="2" fill="#2ea14a"/><circle cx="9" cy="10.5" r="2" fill="#2ea14a"/><path d="M9 2.5 2.5 6.5 9 10.5" fill="none" stroke="#2ea14a"/></svg>Share</span>
      <span class="read">READ MORE</span>
    </div>
  </article>

  <article class="abs post" style="top:2186px">
    <div class="abs date">10<br>JAN</div>
    <h2 class="abs post-title">Lorem ipsum dolor sit amet, consec</h2>
    <p class="abs post-sub">Duis aute irure dolor in reprehenderit</p>
    <div class="abs post-img" role="img" aria-label="Hiker with raised arms on a hilltop above a green valley at sunrise" style="background:linear-gradient(180deg,#dfe6d2,#c9d89a 35%,#7fa83c 60%,#3e6a24 85%,#6a5a48)"></div>
    <p class="abs post-body">Lorem ipsum dolor sit amet, consecit adipiscing elit, sed do eiusmod tempor incidimen labore n dolorme laboris ni ut aliquip ex ena lin consequat Duis aute irure dolor in reprehenderit magna aliqua. Ut enim ad qnexercitation ullamco Neque porro quisquam est, qui dolorem ipsum quia dolor sit amet, conadipi velit sed quia non numquam eius modi tempora incidunt. Quis autem vel eum iure repremInderit in voluptate velit esse quam nihil molestiae consequatur.</p>
    <div class="abs meta">
      <span class="item" style="left:0"><svg width="13" height="13"><rect x="1" y="2" width="10" height="10" fill="none" stroke="#2ea14a" stroke-width="1.6"/><path d="M4 7l2 2 6-7" fill="none" stroke="#2ea14a" stroke-width="1.6"/></svg>Admin</span>
      <span class="item" style="left:113px"><svg width="14" height="13"><ellipse cx="7" cy="6" rx="6.5" ry="5" fill="#2ea14a"/><path d="M3 10l-1 3 4-2z" fill="#2ea14a"/></svg>Leave A Comment</span>
      <span class="item" style="left:292px"><svg width="13" height="13"><rect x="1" y="6" width="3" height="7" fill="#2ea14a"/><path d="M5 6l3-5q2 0 1 4h4v4l-2 4H5z" fill="#2ea14a"/></svg>Like Us</span>
      <span class="item" style="left:411px"><svg width="12" height="13"><circle cx="9" cy="2.5" r="2" fill="#2ea14a"/><circle cx="2.5" cy="6.5" r="2" fill="#2ea14a"/><circle cx="9" cy="10.5" r="2" fill="#2ea14a"/><path d="M9 2.5 2.5 6.5 9 10.5" fill="none" stroke="#2ea14a"/></svg>Share</span>
      <span class="read">READ MORE</span>
    </div>
  </article>

  <div class="abs load"><svg width="16" height="16" viewBox="0 0 16 16"><g stroke="#999" stroke-width="1.6"><line x1="8" y1="1" x2="8" y2="4"/><line x1="8" y1="12" x2="8" y2="15"/><line x1="1" y1="8" x2="4" y2="8"/><line x1="12" y1="8" x2="15" y2="8"/><line x1="3" y1="3" x2="5" y2="5"/><line x1="11" y1="11" x2="13" y2="13"/><line x1="3" y1="13" x2="5" y2="11"/><line x1="11" y1="5" x2="13" y2="3"/></g></svg>Load more blog</div>
</main>

<aside>
  <div class="abs side signup">
    <p>Sign Up To Get Exclusive Lorem Ipsum Dolor Sit Amet, Consecit Adipiscing Elit</p>
    <div class="field">Enter your email address</div>
    <span class="btn-blue">SIGN UP</span>
  </div>

  <h3 class="abs side side-head" style="top:1034px">Recent Posts</h3>
  <div class="abs side recent">
    <ul>
      <li><b>›</b><span>Lorem ipsum dolor sit amet, consecit adipiscing elit</span></li>
      <li><b>›</b><span>Lorem ipsum dolor sit amet, consecit adipiscing elit</span></li>
      <li><b>›</b><span>Lorem ipsum dolor sit amet, consecit adipiscing elit</span></li>
      <li><b>›</b><span>Lorem ipsum dolor sit amet, consecit adipiscing elit</span></li>
    </ul>
    <span class="all">VIEW ALL</span>
  </div>

  <div class="abs side social">
    <div class="tabs">
      <span class="on"><i></i>Friends</span>
      <span class="off"><i></i>Chirps</span>
      <span class="off"><i></i>Snaps</span>
    </div>
    <div class="feed">
      <div class="row"><div class="avatar" role="img" aria-label="Member profile photo" style="background:#c9a58a"></div><div><p>Lorem Ipsum is simply dummy text of the printing..</p><span class="like">Like</span></div></div>
      <div class="row"><div class="avatar" role="img" aria-label="Member profile photo" style="background:#6e4a3c"></div><div><p>Lorem Ipsum is simply dummy text of the printing..</p><span class="like">Like</span></div></div>
      <div class="row"><div class="avatar" role="img" aria-label="Member profile photo" style="background:#d8c2ae"></div><div><p>Lorem Ipsum is simply dummy text of the printing..</p><span class="like">Like</span></div></div>
      <div class="row"><div class="avatar" role="img" aria-label="Member profile photo" style="background:#5a3a30"></div><div><p>Lorem Ipsum is simply dummy text of the printing..</p><span class="like">Like</span></div></div>
    </div>
  </div>

  <div class="abs side query">
    <h4>Send Us Your Query</h4>
    <div class="field">Enter your name</div>
    <div class="field">Enter your email address</div>
    <div class="field area">Enter your query</div>
    <span class="btn-green">SEND</span>
  </div>

  <h3 class="abs side side-head" style="top:1958px;left:794px">Tags</h3>
  <div class="abs side tags">
    <span style="font-size:18px">Health</span><span style="font-size:18px">Health food</span><span style="font-size:12px">friday</span><br>
    <span style="font-size:13px">monday</span><span style="font-size:18px">Diets</span><span style="font-size:15px">Health Facts</span><br>
    <span style="font-size:19px">Eat</span><span style="font-size:11px">wednesday</span><span style="font-size:16px">motivational</span><br>
    <span style="font-size:16px">Cleanes</span><span style="font-size:16px">Loose It</span><span style="font-size:20px">Obesity</span><br>
    <span style="font-size:14px">Fast diets</span><span style="font-size:20px">Workouts</span><span style="font-size:12px">Spinach</span>
  </div>

  <div class="abs side ad">
    <span class="maker">Plainleaf</span>
    <div class="photo" role="img" aria-label="Product photo of a halved avocado"></div>
    <span class="tag1">soothes</span>
    <span class="tag2">irritated skin</span>
  </div>
</aside>

<footer class="abs footer">Copyright© 2017 Bright Years Media. All rights reserved.</footer>

</body>
</html>
```